Design für Sprüche Darstellung
Zielgruppe
www.wortblick-heute.org ist eine der größten Sprüche Seiten im Netz. Mit monatlich ca. 800.000 Aufrufen.
Für unsere Plauderbook Seite (https://www.facebook.com/WortblickHeute/) suchen wir ein neues Spruch Design für unsere Posts.
Wie Sie auf der Plauderbook Seite sehen, erstellen wir viele Spruchbilder bereits mit passenden Hintergründen.
Ihr Aufgabe ist es ein Design zu entwerfen, dass wir für die übrigen Sprüche verwenden möchten. Also für die Sprüche, die kein extra Spruchbild mit Hintergrund bekommen.
Diese sollen trotzdem auch durch kreative Schriftarten und Gestaltung Aufmerksamkeit generieren.
Aufgabenstellung
Erstellung einer quadratischen Photoshop Vorlage die für eine Vielzahl an Sprüchen und Zitaten verwendet werden kann.
Passender Hintergrund + Schriftart.
Weiterhin soll unser Logo sowie die Webadresse mit darauf platziert werden.

```html
<!DOCTYPE html>
<html lang="de">
<head>
<meta charset="utf-8">
<title>Wortblick Heute – Spruchvorlage</title>
<link rel="stylesheet" href="https://fonts.googleapis.com/css2?family=Bebas+Neue&family=Raleway:wght@400&display=swap">
<style>
  :root {
    --sky-light: #c3ccd2;
    --sky-mid: #7f93a8;
    --deep-blue: #34506f;
    --night-blue: #253a55;
    --warm-glow: rgba(246, 232, 196, 0.55);
    --text-white: #ffffff;
  }
  html, body {
    margin: 0;
    padding: 0;
    width: 1200px;
    height: 1200px;
    overflow: hidden;
  }
  .post {
    position: relative;
    width: 1200px;
    height: 1200px;
    overflow: hidden;
    color: var(--text-white);
  }
  .post-background {
    position: absolute;
    inset: 0;
    background:
      radial-gradient(ellipse 55% 30% at 35% 14%, var(--warm-glow), transparent 70%),
      radial-gradient(ellipse 40% 30% at 90% 40%, rgba(240, 228, 200, 0.35), transparent 70%),
      linear-gradient(180deg, var(--sky-light) 0%, var(--sky-mid) 30%, var(--deep-blue) 62%, var(--night-blue) 100%);
  }
  .quote {
    position: absolute;
    top: 455px;
    left: 0;
    width: 100%;
    margin: 0;
    text-align: center;
    font-family: "Bebas Neue", "Oswald", sans-serif;
    font-weight: 400;
    font-size: 72px;
    line-height: 67px;
    letter-spacing: 1px;
  }
  .quote-author {
    position: absolute;
    top: 702px;
    left: 0;
    width: 100%;
    margin: 0;
    text-align: center;
    font-family: "Raleway", sans-serif;
    font-size: 29px;
  }
  .brand {
    position: absolute;
    top: 982px;
    left: 0;
    width: 100%;
    display: flex;
    justify-content: center;
    align-items: center;
    gap: 18px;
  }
  .brand-mark {
    width: 56px;
    height: 56px;
    background: var(--text-white);
  }
  .brand-name {
    font-family: "Bebas Neue", "Oswald", sans-serif;
    font-size: 74px;
    line-height: 1;
    padding-top: 6px;
  }
  .website {
    position: absolute;
    top: 1097px;
    left: 0;
    width: 100%;
    margin: 0;
    text-align: center;
    font-family: "Raleway", sans-serif;
    font-size: 30px;
  }
</style>
</head>
<body>
  <main class="post">
    <div class="post-background" role="img" aria-label="Unscharfes Stadtlicht-Bokeh in Hellblau, Creme und tiefem Nachtblau"></div>

    <p class="quote">Was immer du tun kannst<br>oder erträumst zu können,<br>beginne es.</p>
    <p class="quote-author">- Johann Wilhelm von Gerthal</p>

    <div class="brand">
      <span class="brand-mark"></span>
      <span class="brand-name">Wortblick Heute</span>
    </div>

    <p class="website">www.wortblick-heute.org</p>
  </main>
</body>
</html>
```